We have developed a fully functional App called Harborwink. However, it requires a nicer GUI. You can see screenshots of our App on www.harborwink-example.com under "Tutorial". For those of you with Android, you can also install it. When you go to Harborwink-example.com, your phone will automatically redirect you to download. From there, you'll get a better idea of what our App looks like and how your design can make it way better. Please note we expect a design idea for most screens (there's about 8 screens) but do just one screen first and if you win, you can do the other 8 after.

Target Market(s)

People looking for dating / flirting

Industry/Entity Type

Android

Requirements
Must have
• sleek looking

```html
<!DOCTYPE html>
<html lang="en">
<head>
<meta charset="utf-8">
<title>Harborwink – Main</title>
<link rel="stylesheet" href="https://fonts.googleapis.com/css2?family=Roboto:ital,wght@0,400;0,500;0,700;1,700&display=swap">
<style>
  :root{
    --page:#f1f1f1;
    --black:#000;
    --white:#fff;
    --bar:#e8e8e8;
    --bar-line:#d2d2d2;
    --blue:#0f5f94;
    --pink:#c4127a;
    --grey-badge:#8c8c8c;
    --text:#333;
    --divider:#dedede;
    --search-band:#bcbcbc;
    --icon:#8f8f8f;
  }
  *{box-sizing:border-box;margin:0;padding:0}
  html,body{width:768px;height:1200px;overflow:hidden;background:var(--page);font-family:"Roboto",sans-serif}
  .screen{position:absolute;left:48px;top:0;width:672px;height:1200px;background:var(--white);display:flex;flex-direction:column;overflow:hidden}

  .status-bar{height:45px;background:var(--black);color:var(--white);display:flex;align-items:center;justify-content:space-between;padding:0 18px;font-size:18px;font-weight:500}
  .status-left,.status-right{display:flex;align-items:center;gap:8px;width:200px}
  .status-right{justify-content:flex-end}
  .signal{display:flex;gap:3px}
  .signal i{width:11px;height:11px;border-radius:50%;background:var(--white);display:block}
  .signal i.off{background:none;border:1.5px solid var(--white)}
  .battery{width:48px;height:20px;border:2px solid var(--white);border-radius:4px;padding:2px;position:relative}
  .battery::before{content:"";display:block;height:100%;background:var(--white);border-radius:1px}
  .battery::after{content:"";position:absolute;right:-5px;top:5px;width:3px;height:7px;background:var(--white);border-radius:0 2px 2px 0}

  .app-header{height:78px;background:var(--bar);display:flex;align-items:stretch;border-bottom:1px solid var(--bar-line)}
  .header-btn{width:80px;display:flex;align-items:center;justify-content:center}
  .header-btn.menu{border-right:1px solid var(--bar-line)}
  .header-btn.swap{border-left:1px solid var(--bar-line)}
  .brand{flex:1;display:flex;align-items:center;justify-content:center;gap:12px}
  .brand-dot{width:26px;height:26px;border-radius:50%;background:var(--pink)}
  .brand-name{font-size:32px;font-weight:400;color:var(--blue)}

  .member-list{list-style:none;flex:1;overflow:hidden}
  .member{height:148px;border-bottom:1px solid var(--divider);display:flex;align-items:center;position:relative;padding-left:21px}
  .avatar{width:106px;height:106px;border-radius:50%;flex:none;position:relative}
  .avatar .photo{width:100%;height:100%;border-radius:50%;display:block}
  .unread{position:absolute;left:-1px;top:8px;width:17px;height:17px;border-radius:50%;background:var(--pink);color:var(--white);font-size:10px;font-weight:700;display:flex;align-items:center;justify-content:center}
  .info{margin-left:29px;width:450px}
  .headline{display:flex;align-items:center;gap:8px;font-size:18px;color:#555;margin-bottom:8px}
  .username{color:var(--blue);font-weight:400}
  .tag{font-size:8px;font-weight:700;color:var(--white);text-transform:uppercase;padding:3px 9px;border-radius:3px;background:var(--grey-badge);letter-spacing:.2px}
  .tag.online{background:var(--pink)}
  .bio{font-size:14px;line-height:21px;color:var(--text);letter-spacing:-.1px}
  .city{font-size:11.5px;font-weight:700;font-style:italic;color:#222;margin-top:5px}
  .chevron{position:absolute;right:22px;top:50%;transform:translateY(-50%)}
  .member.peek{height:48px;align-items:flex-start;border-bottom:none}
  .member.peek .avatar{margin-top:22px}
  .member.peek .headline{margin-top:26px}

  .search-band{height:62px;background:var(--search-band);display:flex;align-items:center;padding:0 21px}
  .search-field{flex:1;height:42px;background:var(--white);border-radius:3px 0 0 3px;font-size:13px;font-style:italic;color:#9a9a9a;display:flex;align-items:center;padding-left:10px}
  .search-btn{width:78px;height:42px;background:var(--blue);border-radius:0 3px 3px 0;display:flex;align-items:center;justify-content:center}

  .tab-bar{height:78px;background:var(--bar);display:flex}
  .tab{flex:1;display:flex;flex-direction:column;align-items:center;justify-content:center;gap:6px;font-size:13px;font-weight:700;color:var(--icon);border-left:1px solid var(--bar-line)}
  .tab:first-child{border-left:none}
  .tab.active{color:var(--blue)}
  .tab-icon{position:relative;height:30px;display:flex;align-items:center}
  .count{position:absolute;right:-12px;top:-4px;width:17px;height:17px;border-radius:50%;background:var(--pink);color:var(--white);font-size:10px;display:flex;align-items:center;justify-content:center}
</style>
</head>
<body>
<div class="screen">
  <div class="status-bar">
    <div class="status-left">
      <span class="signal"><i></i><i></i><i></i><i></i><i class="off"></i></span>
      <span>Carrier</span>
      <svg width="20" height="15" viewBox="0 0 20 15"><path d="M10 14l3-3.5a4.5 4.5 0 0 0-6 0z" fill="#fff"/><path d="M4.5 8.5a8 8 0 0 1 11 0M1.5 5a12.5 12.5 0 0 1 17 0" stroke="#fff" stroke-width="2" fill="none"/></svg>
    </div>
    <span>5:30PM</span>
    <div class="status-right">
      <svg width="22" height="20" viewBox="0 0 22 20"><circle cx="11" cy="10" r="8" stroke="#fff" stroke-width="2" fill="none"/><rect x="7.5" y="9" width="7" height="5" fill="#fff"/><path d="M9 9V7.5a2 2 0 0 1 4 0V9" stroke="#fff" stroke-width="1.5" fill="none"/></svg>
      <span>100%</span>
      <span class="battery"></span>
    </div>
  </div>

  <header class="app-header">
    <div class="header-btn menu">
      <svg width="30" height="24" viewBox="0 0 30 24" fill="#8a8a8a"><rect x="0" y="1" width="4" height="3"/><rect x="7" y="1" width="23" height="3"/><rect x="0" y="7" width="4" height="3"/><rect x="7" y="7" width="23" height="3"/><rect x="0" y="13" width="4" height="3"/><rect x="7" y="13" width="23" height="3"/><rect x="0" y="19" width="4" height="3"/><rect x="7" y="19" width="23" height="3"/></svg>
    </div>
    <div class="brand"><span class="brand-dot"></span><span class="brand-name">Harborwink</span></div>
    <div class="header-btn swap">
      <svg width="30" height="26" viewBox="0 0 30 26" fill="none" stroke="#8a8a8a" stroke-width="3"><path d="M4 8h20M18 2l6 6-6 6"/><path d="M26 18H6M12 12l-6 6 6 6"/></svg>
    </div>
  </header>

  <ul class="member-list">
    <li class="member">
      <div class="avatar"><span class="photo" role="img" aria-label="Profile photo of SweetGuy85" style="background:radial-gradient(circle at 50% 55%,#d6a98b,#4a3a33 75%)"></span></div>
      <div class="info">
        <div class="headline"><span class="username">SweetGuy85</span><span>// 29</span><span class="tag online">Online</span></div>
        <p class="bio">Lorem ipsum dolor sit amet, consectetur adipiscing elit. Sed quis faucibus magna. Integer vel accumsan nulla. Praesent scelerisque...</p>
        <p class="city">New York, U.S.A.</p>
      </div>
      <svg class="chevron" width="22" height="50" viewBox="0 0 22 50"><path d="M2 2l18 23L2 48" stroke="#c9c9c9" stroke-width="2" fill="none"/></svg>
    </li>
    <li class="member">
      <div class="avatar"><span class="photo" role="img" aria-label="Profile photo of HonestGirl" style="background:radial-gradient(circle at 50% 55%,#e0b49a,#3b2a24 78%)"></span><span class="unread">3</span></div>
      <div class="info">
        <div class="headline"><span class="username">HonestGirl</span><span class="tag online">Online</span></div>
        <p class="bio">In ornare euismod turpis, vel tristique augue malesuada id. Nulla eu neque ligula. Nulla nec viverra ligula. Nunc ut mattis turpis...</p>
        <p class="city">Sacramento, U.S.A.</p>
      </div>
      <svg class="chevron" width="22" height="50" viewBox="0 0 22 50"><path d="M2 2l18 23L2 48" stroke="#c9c9c9" stroke-width="2" fill="none"/></svg>
    </li>
    <li class="member">
      <div class="avatar"><span class="photo" role="img" aria-label="Profile photo of Mimi" style="background:radial-gradient(circle at 50% 50%,#ecd2bf,#b69a7c 80%)"></span></div>
      <div class="info">
        <div class="headline"><span class="username">Mimi</span><span>// 25</span><span class="tag">2hrs ago</span></div>
        <p class="bio">Class aptent taciti sociosqu ad litora torquent per conubia nostra, per inceptos himenaeos. Donec faucibus lacus vitae dolor luctus, at...</p>
        <p class="city">Chicago, U.S.A.</p>
      </div>
      <svg class="chevron" width="22" height="50" viewBox="0 0 22 50"><path d="M2 2l18 23L2 48" stroke="#c9c9c9" stroke-width="2" fill="none"/></svg>
    </li>
    <li class="member">
      <div class="avatar"><span class="photo" role="img" aria-label="Profile photo of CoCo" style="background:radial-gradient(circle at 50% 50%,#f3e2d6,#d9b99c 80%)"></span></div>
      <div class="info">
        <div class="headline"><span class="username">CoCo</span><span>// 31</span><span class="tag">2 days ago</span></div>
        <p class="bio">Pellentesque porta libero sollicitudin lacus pellentesque, id convallis magna consectetur. Mauris convallis tellus augue, sit amet dapibus...</p>
        <p class="city">Boston, U.S.A.</p>
      </div>
      <svg class="chevron" width="22" height="50" viewBox="0 0 22 50"><path d="M2 2l18 23L2 48" stroke="#c9c9c9" stroke-width="2" fill="none"/></svg>
    </li>
    <li class="member">
      <div class="avatar"><span class="photo" role="img" aria-label="Profile photo of RayMoon" style="background:radial-gradient(circle at 60% 60%,#c99a78,#2a2420 75%)"></span></div>
      <div class="info">
        <div class="headline"><span class="username">RayMoon</span><span>// 22</span><span class="tag">30 mins ago</span></div>
        <p class="bio">Nullam et accumsan erat. Phasellus et arcu tortor. Mauris commodo, ante varius consequat sollicitudin, metus nunc pellentesque nisl, ut...</p>
        <p class="city">Los Angeles, U.S.A.</p>
      </div>
      <svg class="chevron" width="22" height="50" viewBox="0 0 22 50"><path d="M2 2l18 23L2 48" stroke="#c9c9c9" stroke-width="2" fill="none"/></svg>
    </li>
    <li class="member">
      <div class="avatar"><span class="photo" role="img" aria-label="Profile photo of Wavecatcher" style="background:radial-gradient(circle at 50% 55%,#d4a27a,#556b3a 82%)"></span><span class="unread">1</span></div>
      <div class="info">
        <div class="headline"><span class="username">Wavecatcher</span><span class="tag">1 wk ago</span></div>
        <p class="bio">In ornare euismod turpis, vel tristique augue malesuada id. Nulla eu neque ligula. Nulla nec viverra ligula. Nunc ut mattis turpis...</p>
        <p class="city">San Diego, U.S.A.</p>
      </div>
      <svg class="chevron" width="22" height="50" viewBox="0 0 22 50"><path d="M2 2l18 23L2 48" stroke="#c9c9c9" stroke-width="2" fill="none"/></svg>
    </li>
    <li class="member peek">
      <div class="avatar"><span class="photo" role="img" aria-label="Profile photo of Meow" style="background:radial-gradient(circle at 50% 40%,#ecd8c2,#c9a985 80%)"></span></div>
      <div class="info">
        <div class="headline"><span class="username">Meow</span><span class="tag">1 hr ago</span></div>
      </div>
    </li>
  </ul>

  <div class="search-band">
    <div class="search-field">Search...</div>
    <div class="search-btn">
      <svg width="24" height="24" viewBox="0 0 24 24"><circle cx="10" cy="10" r="6.5" stroke="#fff" stroke-width="3" fill="none"/><path d="M15 15l6 6" stroke="#fff" stroke-width="3.5" stroke-linecap="round"/></svg>
    </div>
  </div>

  <nav class="tab-bar">
    <div class="tab active">
      <span class="tab-icon"><svg width="34" height="30" viewBox="0 0 34 30"><path d="M17 2L2 15h4v13h8v-8h6v8h8V15h4z" fill="#0f5f94"/></svg></span>
      <span>MAIN</span>
    </div>
    <div class="tab">
      <span class="tab-icon"><svg width="30" height="22" viewBox="0 0 30 22"><rect x="1" y="1" width="28" height="20" rx="1" fill="#8f8f8f"/><path d="M1 2l14 11L29 2" stroke="#e8e8e8" stroke-width="2" fill="none"/></svg><span class="count">5</span></span>
      <span>MESSAGE</span>
    </div>
    <div class="tab">
      <span class="tab-icon"><svg width="30" height="30" viewBox="0 0 30 30"><g fill="#8f8f8f"><circle cx="15" cy="15" r="9"/><rect x="12.5" y="2" width="5" height="26" rx="1"/><rect x="12.5" y="2" width="5" height="26" rx="1" transform="rotate(45 15 15)"/><rect x="12.5" y="2" width="5" height="26" rx="1" transform="rotate(90 15 15)"/><rect x="12.5" y="2" width="5" height="26" rx="1" transform="rotate(135 15 15)"/></g><circle cx="15" cy="15" r="4" fill="#e8e8e8"/></svg></span>
      <span>SETTINGS</span>
    </div>
  </nav>
</div>
</body>
</html>
```